Modern & Simple Essential Oils Label

Company Name: Meadowlark Essentials

What we sell: Aromatherapy products, pure therapeutic essential oils.

Design need:
We are looking for a creative and youthful design for the labels used on small essentials oils.

I have two sizes of bottles that I use for essential oils a 5ml bottle and a 15ml bottle. They are dark Amber color glass with black lids. I like the clear labels or mayble a dark brown background. With white or clear lettering with punch of color too! Each oil type is represented by different color. (lavender- purple, lemon - yellow). The label will be the same for all the oils in the two sizes with only a different oil name & coordinating color.
5ml label size should be: 1 " x 2.625"
15ml label size should be: 1.5" x 3.5"

I have some labels that I have had another designer start on, but they aren't quite what I want and missing that something (alot!).. I don't know what. Interest maybe? Lack of design? I dunno.. they are attached. Maybe it's the logo? I don't know! But its gotta change! When I cut out a proof and put a sample on the bottle as I look straight on at the label all I see is a big dot, no logo.. nothing interesting.
Updates

Project Deadline Extended
Reason: Hi! Id like to extend this deadline. Ive been unavailable for a few days due to an illness and Im so far behind! Im feeling MUCH better and looking forward to getting caught up and move with the project. Im not sure how this works, but I attached a list of the oils that we currently have available. And in the list is the idea for the color schemes for the oils. The basic idea is for it to have a wide array of colors, so using different shades of greens, yellows, oranges and so on. So that its like a rainbow. We are not set of that particular color for that particular oil. It was just a idea list of possible colors for oils. Thanks so much!

Target Market(s)

Metro & Modern people. Interested in healthy organic living, Mostly women (some men) 20-45 who are interested in holistic healing.

Industry/Entity Type

It Company

Requirements
Must have
• A reputable look. Clean, organic, crisp, zen or spa-like feel. Modern, youthful appealing label design. Approachable and interesting, not intimidating so that I don't turn away people who are new or not familiar with how to use essential oils.
Should not have
• do NOT want the look to be anywhere close to medicinal, witchy, crafty, hippie, mystical, overly earthy, magical, or voodoo. Do not want it to look like something out of a grandmothers medicine cabinet.

```html
<!DOCTYPE html>
<html lang="en">
<head>
<meta charset="UTF-8">
<title>Meadowlark Essentials – Lemongrass Label</title>
<link rel="stylesheet" href="https://fonts.googleapis.com/css2?family=Roboto+Condensed:wght@400&family=Roboto:wght@500&family=Cinzel:wght@400&family=Source+Sans+3:wght@400&display=swap">
<style>
  :root {
    --brown: #3f2a1c;
    --green: #a9c31a;
    --white: #ffffff;
    --paper: #ffffff;
  }
  * { margin: 0; padding: 0; box-sizing: border-box; }
  html, body {
    width: 1200px; height: 900px; overflow: hidden;
    background: var(--paper);
  }
  .canvas { position: relative; width: 1200px; height: 900px; }

  .brand {
    position: absolute; display: flex; align-items: center;
    font-family: "Roboto", sans-serif; font-weight: 500;
    text-transform: uppercase; white-space: nowrap;
  }
  .brand-mark { border-radius: 50%; flex: none; }

  .brand--header {
    left: 0; width: 1200px; top: 180px; height: 50px;
    justify-content: center; gap: 20px;
    font-size: 34px; letter-spacing: 0.5px; color: var(--brown);
  }
  .brand--header .brand-mark { width: 44px; height: 44px; background: var(--brown); }

  .label {
    position: absolute; left: 90px; top: 330px;
    width: 1020px; height: 400px; background: var(--brown);
  }

  .facts {
    position: absolute; left: 16px; top: 16px; width: 600px;
    font-family: "Roboto Condensed", sans-serif; color: var(--white);
    font-size: 19px; line-height: 32px;
  }
  .facts-rule {
    position: absolute; left: 16px; top: 120px;
    width: 590px; height: 4px; background: var(--white);
  }
  .usage, .caution, .address {
    position: absolute; left: 16px; width: 600px;
    font-family: "Roboto Condensed", sans-serif; color: var(--white);
    font-size: 19px; line-height: 31px;
  }
  .usage { top: 140px; }
  .caution { top: 230px; }
  .address { top: 359px; }

  .brand--label {
    left: 680px; top: 48px; gap: 10px;
    font-size: 23px; color: var(--white);
  }
  .brand--label .brand-mark { width: 26px; height: 26px; background: var(--white); }

  .oil-panel {
    position: absolute; left: 634px; top: 120px;
    width: 386px; height: 190px; background: var(--green);
    text-align: center; color: var(--brown);
  }
  .oil-name {
    margin-top: 34px;
    font-family: "Cinzel", serif; font-size: 40px; line-height: 48px;
    color: var(--white); letter-spacing: 1px;
  }
  .oil-detail {
    margin-top: 10px;
    font-family: "Source Sans 3", sans-serif; font-size: 22px; line-height: 30px;
    color: var(--brown);
  }
  .volume {
    position: absolute; left: 634px; width: 386px; top: 345px;
    text-align: center;
    font-family: "Source Sans 3", sans-serif; font-size: 24px; color: var(--white);
  }
</style>
</head>
<body>
<main class="canvas">
  <div class="brand brand--header">
    <span>Meadowlark</span><span class="brand-mark"></span><span>Essentials</span>
  </div>

  <section class="label">
    <div class="facts">
      <p>Supplemental Facts</p>
      <p>Serving Size: 1 drop / Servings Per Container: about 85</p>
      <p>Oil: Cymbopogon Flexuosu</p>
    </div>
    <div class="facts-rule"></div>

    <p class="usage">For aromatic, topical use. 100% pure therapeutic-grade essential oil.<br>Dilute with a carrier oil before using.</p>

    <p class="caution">CAUTION: For External Use Only. Not for Ingestion. Keep away from eyes<br>and mucous membranes. May cause skin sensitivity. If pregnant consult<br>physician before use. Keep out of reach of children. Keep away from flame.</p>

    <p class="address">Meadowlark Essentials P.O. Box 442, Fairbrook, CO 80917</p>

    <div class="brand brand--label">
      <span>Meadowlark</span><span class="brand-mark"></span><span>Essentials</span>
    </div>

    <div class="oil-panel">
      <h1 class="oil-name">Lemongrass</h1>
      <p class="oil-detail">Cymbopogon Flexuosus<br>100% Pure Essential Oil</p>
    </div>

    <p class="volume">5ml</p>
  </section>
</main>
</body>
</html>
```